Dog themed post card for homeowners that may be willing to sell their house.

We will be sending these postcards to homeowners that may be interested in selling their house. Our business is themed around our dog "Biscuit"- Biscuit Gets Homes. We are using her as the focal point of the business because typically these homeowners get lots of mailers that are similar and we would like stand out with an inviting puppy dog.
We would like to included the icon for Chirpbook and Snapgrid with her handle "@BiscuitGetsHomes" and her website BiscuitGetsHomes-example.com and our phone number 555-482-1976.
We will be sending these postcards in batches to various subdivisions. For that reason please consider a format that can easily change the name of the subdivision. We are including the subdivision name because we want the postcard to be slightly more personal/targeted.
Our business is just starting and we would like to get some brand recognition going. We envision Biscuit Gets Homes predominately displayed somehow.
I have attached numerous pictures of Biscuit. We envision using one on each side of the postcard. Below are phrases we would like to include on the postcard in a format that you see fitting. Please use the verbiage below and not what is sketched on the uploaded postcard. The below verbiage is the most up to date.
-I recently bought a house in (subdivision name) and would love to buy yours.
-Call my humans today so we can give you a no obligation offer
-No money out of your pocket
-Quick closing
-Any condition
-Can help with moving expenses

Target Market(s)

Home owners with equity in their house that may need to sell quickly. These are generally people that do not enjoy the buying/selling of real estate. It can sometimes be someone who has recently inherited a home and doesnt want to deal with the headache. Other times it may be someone going through a divorce or forclosure and want to sell their home quickly.

Industry/Entity Type

Direct Marketing

Requirements
Must have
• Happy and bright feel. This industry is saturated with less than ethical people and we are trying to convey a very clean, honest, straight forward and scam-free process.

```html
<!DOCTYPE html>
<html lang="en">
<head>
<meta charset="utf-8">
<title>Biscuit Gets Homes – Postcard</title>
<link href="https://fonts.googleapis.com/css2?family=Jost:wght@400;500;700;800&family=Fredoka:wght@600&display=swap" rel="stylesheet">
<style>
:root{
  --stage:#5a5a5a;
  --cream:#fdfbe8;
  --orange:#ef7a0a;
  --orange-bright:#f7861c;
  --green:#adb80c;
  --yellow:#f9b800;
  --ink:#2a2a2a;
  --rule:#9a9a9a;
  --white:#ffffff;
  --brand:#d4660a;
}
*{box-sizing:border-box;margin:0;padding:0}
html,body{width:873px;height:1200px;overflow:hidden;background:var(--stage)}
body{position:relative;font-family:"Jost",sans-serif}
.card{position:absolute;left:97px;width:678px;height:484px;overflow:hidden}
.card--front{top:91px;background:var(--cream)}
.card--back{top:631px;background:linear-gradient(90deg,var(--cream),var(--white) 65%)}
.card svg.shapes{position:absolute;inset:0}
.photo{position:absolute;border-radius:50%;border:3px solid var(--white)}
.photo--front{left:335px;top:18px;width:370px;height:370px;background:radial-gradient(circle at 60% 60%,#b9a88e,#c9ccd0 45%,#e6e8ea)}
.photo--back-main{left:18px;top:29px;width:324px;height:316px;background:radial-gradient(circle at 45% 60%,#bfc0c6,#d9dcdc 50%,#a49a84)}
.photo--back-small{left:245px;top:226px;width:172px;height:172px;background:radial-gradient(circle at 50% 55%,#c2c3c8,#d8d9d6 55%,#8c8a72)}
.brand{position:absolute;left:36px;top:22px;color:var(--brand);font-weight:800;line-height:.95;letter-spacing:-.5px}
.brand__name{display:block;font-size:64px}
.brand__tail{display:block;font-size:44px;text-transform:uppercase}
.pitch{position:absolute;left:39px;top:171px;height:79px;border-left:3px solid #b98a12;padding-left:13px;color:var(--ink);line-height:1.05}
.pitch__small{font-size:12px}
.pitch__big{font-family:"Fredoka",sans-serif;font-weight:600;font-size:16px;color:var(--orange)}
.pitch__mid{font-size:17px;font-weight:500;color:var(--orange)}
.pitch__mid span{color:var(--ink)}
.bubble{position:absolute;inset:0;pointer-events:none}
.thought{position:absolute;left:198px;top:199px;width:160px;text-align:center;color:var(--white);font-size:16px;font-weight:500;line-height:21px;letter-spacing:.2px}
.perks{position:absolute;left:40px;top:348px;display:grid;grid-template-columns:163px 150px;row-gap:14px;list-style:none}
.perk{display:flex;align-items:center;gap:9px;color:var(--white);font-size:13px;line-height:18px}
.perk__icon{width:32px;height:32px;flex:none}
.contact-bar{position:absolute;left:38px;top:447px;display:flex;align-items:center;gap:9px;color:var(--white);font-size:13px;white-space:nowrap}
.contact-bar .sep{opacity:.9}
.dot{display:inline-block;width:14px;height:14px;border-radius:50%;background:var(--white)}
.ico{width:15px;height:15px;flex:none}
.stamp{position:absolute;left:556px;top:37px;width:85px;height:90px;border:1px solid #cfcfcf}
.address-line{position:absolute;left:455px;width:186px;border-top:1px solid var(--rule)}
.contact{position:absolute;left:86px;top:352px;width:200px;text-align:center;color:var(--white)}
.contact__title{font-family:"Fredoka",sans-serif;font-weight:600;font-size:22px;line-height:30px;padding-bottom:2px;border-bottom:1.5px solid var(--white);margin:0 25px 6px}
.contact__row{display:flex;justify-content:center;align-items:center;gap:6px;font-size:13px;line-height:24px;white-space:nowrap}
</style>
</head>
<body>

<section class="card card--front">
  <svg class="shapes" viewBox="0 0 678 484" aria-hidden="true">
    <defs>
      <linearGradient id="silver" x1="0" x2="1">
        <stop offset="0" stop-color="#8c8c8c"/><stop offset=".6" stop-color="#d8d8d8"/><stop offset="1" stop-color="#f4f4f4"/>
      </linearGradient>
      <linearGradient id="silverR" x1="0" x2="1">
        <stop offset="0" stop-color="#f2f2f2"/><stop offset="1" stop-color="#8e8e8e"/>
      </linearGradient>
    </defs>
    <circle cx="520" cy="203" r="212" fill="var(--green)"/>
    <circle cx="520" cy="203" r="192" fill="var(--white)"/>
    <path d="M0,300 C110,262 220,250 300,262 L300,275 C220,268 110,282 0,318 Z" fill="url(#silver)"/>
    <path d="M0,332 C120,282 260,268 360,302 C460,336 560,420 678,437 L678,484 L0,484 Z" fill="var(--orange)"/>
    <path d="M0,318 C110,282 220,268 300,275 L300,282 C210,276 110,290 0,332 Z" fill="var(--white)"/>
    <path d="M400,330 C500,395 590,410 678,397 L678,427 C580,438 490,420 400,330 Z" fill="url(#silverR)"/>
    <path d="M400,330 C490,420 580,438 678,427 L678,437 C570,430 470,400 400,330 Z" fill="var(--white)"/>
  </svg>

  <div class="photo photo--front" role="img" aria-label="Photo of Biscuit, a fluffy grey and white dog in a striped bandana, sitting in front of a white house"></div>

  <svg class="bubble" viewBox="0 0 678 484" aria-hidden="true">
    <g transform="translate(279 252) scale(0.85) translate(-280 -255)">
      <g stroke="#222" stroke-width="5">
        <circle cx="232" cy="205" r="40"/><circle cx="287" cy="188" r="45"/><circle cx="337" cy="212" r="38"/>
        <circle cx="352" cy="262" r="40"/><circle cx="332" cy="305" r="38"/><circle cx="277" cy="322" r="42"/>
        <circle cx="222" cy="302" r="40"/><circle cx="205" cy="252" r="40"/>
      </g>
      <g fill="var(--green)">
        <circle cx="232" cy="205" r="40"/><circle cx="287" cy="188" r="45"/><circle cx="337" cy="212" r="38"/>
        <circle cx="352" cy="262" r="40"/><circle cx="332" cy="305" r="38"/><circle cx="277" cy="322" r="42"/>
        <circle cx="222" cy="302" r="40"/><circle cx="205" cy="252" r="40"/><circle cx="280" cy="255" r="72"/>
      </g>
      <g fill="none" stroke="#222" stroke-width="3">
        <circle cx="370" cy="322" r="11"/><circle cx="392" cy="338" r="8"/><circle cx="418" cy="333" r="4"/>
        <path d="M354,176 C382,189 396,214 400,240"/><path d="M180,300 C180,315 188,325 194,330"/>
      </g>
    </g>
  </svg>

  <h1 class="brand"><span class="brand__name">Biscuit</span><span class="brand__tail">Gets Homes</span></h1>

  <div class="pitch">
    <div class="pitch__small">Call my</div>
    <div class="pitch__big">HUMANS TODAY</div>
    <div class="pitch__small">so they can give you</div>
    <div class="pitch__mid"><span>a</span> no obligation</div>
    <div class="pitch__small">cash offer</div>
  </div>

  <p class="thought">I recently<br>bought a house in<br>Maple Hollow and<br>would love<br>to buy yours.</p>

  <ul class="perks">
    <li class="perk">
      <svg class="perk__icon" viewBox="0 0 32 32" fill="none" stroke="#fff" stroke-width="1.3"><circle cx="16" cy="16" r="15"/><rect x="9" y="12" width="14" height="10" rx="1.5"/><path d="M11 12l8-4 2 4M19 16h4v3h-4z"/></svg>
      <span>No money out<br>of your pocket</span>
    </li>
    <li class="perk">
      <svg class="perk__icon" viewBox="0 0 32 32" fill="none" stroke="#fff" stroke-width="1.3"><circle cx="16" cy="16" r="15"/><circle cx="16" cy="17" r="7"/><path d="M14 8h4M16 10v0M16 17l2-3M7 15h3M6 18h3"/></svg>
      <span>Quick<br>Closing</span>
    </li>
    <li class="perk">
      <svg class="perk__icon" viewBox="0 0 32 32" fill="none" stroke="#fff" stroke-width="1.3"><circle cx="16" cy="16" r="15"/><circle cx="17" cy="11" r="4"/><path d="M7 21l5-3h6l-1 2h-4M7 21l3 3 10-3 5-5"/></svg>
      <span>I can help with<br>moving expenses</span>
    </li>
    <li class="perk">
      <svg class="perk__icon" viewBox="0 0 32 32" fill="none" stroke="#fff" stroke-width="1.3"><circle cx="16" cy="16" r="15"/><path d="M7 14l5-4 4 2 4-2 5 4M9 16l5 5 2-1 4-3 3-3M13 15l3 3"/></svg>
      <span>Any<br>Condition</span>
    </li>
  </ul>

  <div class="contact-bar">
    <svg class="ico" viewBox="0 0 16 16" fill="none" stroke="#fff" stroke-width="1.1"><circle cx="8" cy="8" r="7"/><ellipse cx="8" cy="8" rx="3" ry="7"/><path d="M1 8h14"/></svg>
    <span>BiscuitGetsHomes-example.com</span><span class="sep">|</span>
    <svg class="ico" viewBox="0 0 16 16" fill="none" stroke="#fff" stroke-width="1.1"><circle cx="8" cy="8" r="7"/><path d="M5.5 4.5l1.5 2-1 1c.6 1.3 1.4 2.1 2.6 2.6l1-1 2 1.5-1 1.4C7.8 12 4.4 8.6 4.1 5.5z"/></svg>
    <span>555-482-1976</span><span class="sep">|</span>
    <span class="dot"></span><span class="dot"></span>
    <span>@BiscuitGetsHomes</span>
  </div>
</section>

<section class="card card--back">
  <svg class="shapes" viewBox="0 0 678 484" aria-hidden="true">
    <circle cx="192" cy="187" r="180" fill="var(--green)"/>
    <circle cx="180" cy="187" r="166" fill="var(--white)"/>
    <circle cx="196" cy="464" r="168" fill="var(--green)"/>
    <circle cx="187" cy="477" r="152" fill="var(--white)"/>
    <circle cx="187" cy="477" r="148" fill="var(--orange-bright)"/>
    <circle cx="339" cy="310" r="99" fill="var(--yellow)"/>
    <circle cx="333" cy="312" r="90" fill="var(--white)"/>
  </svg>

  <div class="photo photo--back-main" role="img" aria-label="Photo of Biscuit sitting on a garden path beside a house"></div>
  <div class="photo photo--back-small" role="img" aria-label="Close photo of Biscuit sitting on a sidewalk"></div>

  <div class="contact">
    <h2 class="contact__title">Contact Us</h2>
    <p class="contact__row">
      <svg class="ico" viewBox="0 0 16 16" fill="none" stroke="#fff" stroke-width="1.1"><circle cx="8" cy="8" r="7"/><path d="M5.5 4.5l1.5 2-1 1c.6 1.3 1.4 2.1 2.6 2.6l1-1 2 1.5-1 1.4C7.8 12 4.4 8.6 4.1 5.5z"/></svg>
      555-482-1976</p>
    <p class="contact__row">
      <svg class="ico" viewBox="0 0 16 16" fill="none" stroke="#fff" stroke-width="1.1"><circle cx="8" cy="8" r="7"/><ellipse cx="8" cy="8" rx="3" ry="7"/><path d="M1 8h14"/></svg>
      BiscuitGetsHomes-example.com</p>
    <p class="contact__row"><span class="dot"></span><span class="dot"></span>@BiscuitGetsHomes</p>
  </div>

  <div class="stamp"></div>
  <div class="address-line" style="top:250px"></div>
  <div class="address-line" style="top:288px"></div>
  <div class="address-line" style="top:327px"></div>
</section>

</body>
</html>
```